Modern Lawfirm Business Card Design

We're looking for a business card to incorporate the newly created logo we had made.

Ideally looking for a law firm business card demonstrating, modern, minimalist, strong/bold design.

I'm open to any design honestly, but nothing "flashy".

Target Market(s)

Immigration law, family immigration, humanitarian, general legal

Industry/Entity Type

Law Firm

Contact Information for Business Card

Please use dummy information, name, street address, city, state, phone number, email, website.

Font styles to use
Serif
Sans Serif

Requirements
Must have
• Please use dummy information, name, street address, city, state, phone number, email, website.

```html
<!DOCTYPE html>
<html lang="en">
<head>
<meta charset="utf-8">
<title>Velarde Immigration Law – Business Card</title>
<link href="https://fonts.googleapis.com/css2?family=Open+Sans:wght@400;600&display=swap" rel="stylesheet">
<style>
  :root {
    --brand-blue: #1e5ea8;
    --map-blue: #3b74b5;
    --ink-grey: #6b6b6b;
    --card-white: #ffffff;
    --page-bg: #2a2a2a;
  }
  * { box-sizing: border-box; margin: 0; padding: 0; }
  html, body { width: 1200px; height: 864px; overflow: hidden; }
  body {
    background: var(--page-bg);
    font-family: "Open Sans", sans-serif;
    position: relative;
  }
  .card {
    position: absolute;
    width: 560px;
    height: 320px;
    box-shadow: 0 10px 30px rgba(0,0,0,.45);
    overflow: hidden;
  }
  /* Front */
  .card-front { left: 90px; top: 70px; background: var(--brand-blue); }
  .world-map {
    position: absolute; left: 40px; top: 20px; width: 480px; height: 270px;
    background: radial-gradient(ellipse at center, var(--map-blue) 0%, rgba(59,116,181,.35) 60%, rgba(59,116,181,0) 80%);
  }
  .front-logo {
    position: absolute; left: 50%; top: 118px; transform: translateX(-50%);
    background: var(--card-white); padding: 14px 26px;
    color: var(--brand-blue); font-weight: 600; font-size: 26px;
    letter-spacing: 2px; white-space: nowrap;
  }
  .front-web {
    position: absolute; left: 0; right: 0; top: 240px; text-align: center;
    color: var(--card-white); font-size: 14px;
  }
  /* Back */
  .card-back { left: 550px; top: 474px; background: var(--card-white); }
  .back-logo {
    position: absolute; left: 30px; top: 28px;
    display: flex; align-items: center; gap: 10px;
    color: var(--brand-blue); font-weight: 600; font-size: 19px; letter-spacing: 1px;
  }
  .logo-square { width: 16px; height: 16px; background: var(--brand-blue); }
  .divider-top {
    position: absolute; left: 170px; right: 30px; top: 96px;
    border-top: 1px solid var(--brand-blue);
  }
  .person { position: absolute; left: 40px; top: 134px; }
  .person-name { color: var(--brand-blue); font-weight: 600; font-size: 21px; }
  .person-title { color: var(--ink-grey); font-size: 14px; margin-top: -2px; }
  .divider-person {
    position: absolute; left: 40px; width: 190px; top: 190px;
    border-top: 1px solid var(--brand-blue);
  }
  .contacts { position: absolute; left: 40px; top: 202px; list-style: none; }
  .contacts li {
    display: flex; align-items: center; gap: 10px;
    color: var(--ink-grey); font-size: 14px; line-height: 24px;
  }
  .contacts svg { width: 14px; height: 14px; stroke: var(--brand-blue); fill: none; stroke-width: 1.6; }
  .address {
    position: absolute; right: 30px; top: 150px; text-align: right;
    color: var(--ink-grey); font-size: 13px; line-height: 19px;
  }
</style>
</head>
<body>
  <section class="card card-front">
    <div class="world-map" role="img" aria-label="Faint world map silhouette across the card"></div>
    <div class="front-logo">VELARDE IMMIGRATION LAW</div>
    <p class="front-web">www.yourwebsite.com</p>
  </section>

  <section class="card card-back">
    <div class="back-logo"><span class="logo-square"></span>VELARDE IMMIGRATION LAW</div>
    <div class="divider-top"></div>
    <div class="person">
      <p class="person-name">Daniel Reyes</p>
      <p class="person-title">President</p>
    </div>
    <div class="divider-person"></div>
    <ul class="contacts">
      <li><svg viewBox="0 0 16 16"><path d="M3 2l3 0 1 3-2 1.5a8 8 0 004 4L10.5 9l3 1v3a1 1 0 01-1 1A11 11 0 012 3a1 1 0 011-1z"/></svg>01 012-345-6789</li>
      <li><svg viewBox="0 0 16 16"><rect x="4" y="1.5" width="8" height="13" rx="1.5"/><line x1="7" y1="12" x2="9" y2="12"/></svg>01 012-345-6780</li>
      <li><svg viewBox="0 0 16 16"><rect x="1.5" y="3.5" width="13" height="9"/><path d="M1.5 3.5l6.5 5 6.5-5"/></svg>info@yourwebsite.com</li>
      <li><svg viewBox="0 0 16 16"><circle cx="8" cy="8" r="6.5"/><ellipse cx="8" cy="8" rx="3" ry="6.5"/><line x1="1.5" y1="8" x2="14.5" y2="8"/></svg>yourwebsite.com</li>
    </ul>
    <p class="address">Street Name, Suite 000<br>State, Zip Code, Country</p>
  </section>
</body>
</html>
```